Ridgely Forge business card for handing simple contact information and generating service awareness

Utilizing the attached logo(s), generate a professional, but approachable, card conveying a sense of capability and integrity. Please only use one logo of the four attached; the different colors are all acceptable, but preference will be given to a design integrating a teal/turquoise logo,

I do not know where to put in the contact information or details?

Target Market(s)

Agriculture, Farming, Timber, Forestry, Construction, Crane Service

Industry/Entity Type

Contact Information for Business Card

Name, Phone Number, email address

Colors

Designer to choose colors to be used in the design.

Requirements
Nice to have
• It would be great to have either a mountain or one of the attached cranes as a backdrop on the rear of the card. Simple watermarks and/or Debossing is also great

```html
<!DOCTYPE html>
<html lang="en">
<head>
<meta charset="utf-8">
<title>Ridgely Forge — Business Card</title>
<link rel="stylesheet" href="https://fonts.googleapis.com/css2?family=Montserrat:wght@400;500;600;700&display=swap">
<style>
  :root {
    --backdrop: #95989b;
    --paper: #ffffff;
    --forest: #2d6e63;
    --ink-light: #ffffff;
  }
  * { margin: 0; padding: 0; box-sizing: border-box; }
  html, body {
    width: 1200px;
    height: 1200px;
    overflow: hidden;
    background: var(--backdrop);
    font-family: "Montserrat", Arial, sans-serif;
  }
  .canvas {
    position: relative;
    width: 1200px;
    height: 1200px;
  }
  .card {
    position: absolute;
    left: 292px;
    width: 623px;
    height: 403px;
  }
  .card--front {
    top: 151px;
    background: var(--paper);
  }
  .card--back {
    top: 654px;
    background: var(--forest);
    color: var(--ink-light);
  }

  /* Front: brand name lockup */
  .brand {
    position: absolute;
    left: 0;
    right: 0;
    top: 170px;
    display: flex;
    align-items: center;
    justify-content: center;
    gap: 16px;
  }
  .brand__dot {
    width: 40px;
    height: 40px;
    border-radius: 50%;
    background: var(--forest);
  }
  .brand__name {
    font-weight: 700;
    font-size: 38px;
    letter-spacing: 1px;
    color: var(--forest);
    text-transform: uppercase;
    line-height: 1;
  }

  /* Back: contact block */
  .person {
    position: absolute;
    right: 355px;
    top: 184px;
    text-align: right;
  }
  .person__name {
    font-weight: 600;
    font-size: 20px;
    letter-spacing: 0.5px;
    line-height: 1.1;
  }
  .person__role {
    font-weight: 400;
    font-size: 15px;
    margin-top: 3px;
  }
  .divider {
    position: absolute;
    left: 269px;
    top: 163px;
    width: 1.5px;
    height: 75px;
    background: var(--ink-light);
  }
  .contact {
    position: absolute;
    left: 299px;
    top: 166px;
    list-style: none;
  }
  .contact__item {
    display: flex;
    align-items: center;
    height: 24px;
    font-size: 15px;
    font-weight: 400;
    letter-spacing: 0.2px;
  }
  .contact__icon {
    width: 22px;
    height: 18px;
    margin-right: 14px;
    flex: none;
  }
</style>
</head>
<body>
<main class="canvas">
  <section class="card card--front" aria-label="Card front">
    <div class="brand">
      <span class="brand__dot"></span>
      <span class="brand__name">Ridgely Forge</span>
    </div>
  </section>

  <section class="card card--back" aria-label="Card back">
    <div class="person">
      <p class="person__name">OWEN HARTLEY</p>
      <p class="person__role">(Founder)</p>
    </div>
    <span class="divider"></span>
    <ul class="contact">
      <li class="contact__item">
        <svg class="contact__icon" viewBox="0 0 22 18" aria-hidden="true">
          <path d="M1 6 C1 1 21 1 21 6 L17 7 L16 4 C13 3 9 3 6 4 L5 7 Z" fill="#fff"/>
          <path d="M5 8 L8 6 H14 L17 8 L19 16 H3 Z" fill="#fff"/>
          <circle cx="11" cy="11.5" r="2.3" fill="#2d6e63"/>
        </svg>
        <span>555-014-2871</span>
      </li>
      <li class="contact__item">
        <svg class="contact__icon" viewBox="0 0 22 18" aria-hidden="true">
          <rect x="1" y="3" width="20" height="13" fill="none" stroke="#fff" stroke-width="1.6"/>
          <path d="M1 3 L11 11 L21 3 M1 16 L8.5 9 M21 16 L13.5 9" fill="none" stroke="#fff" stroke-width="1.6"/>
        </svg>
        <span>hello@ridgelyforge.com</span>
      </li>
      <li class="contact__item">
        <svg class="contact__icon" viewBox="0 0 22 18" aria-hidden="true">
          <circle cx="10" cy="9" r="7.5" fill="none" stroke="#fff" stroke-width="1.6"/>
          <ellipse cx="10" cy="9" rx="3.2" ry="7.5" fill="none" stroke="#fff" stroke-width="1.3"/>
          <path d="M2.5 9 H17.5 M4 5 H16 M4 13 H16" stroke="#fff" stroke-width="1.2"/>
          <path d="M13 9 L13 18 L15 16 L17 19 L18.5 18 L16.5 15 L19 14.5 Z" fill="#fff" stroke="#2d6e63" stroke-width="0.8"/>
        </svg>
        <span>www.ridgelyforge.com</span>
      </li>
    </ul>
  </section>
</main>
</body>
</html>
```